Gentle Willow Pregnancy and Baby Massage

I need a web design for a new business, GENTLE WILLOW PREGNANCY AND BABY MASSAGE that I am in the process of setting up in the suburbs of Perth, Western Australia. The business is owned and operated by myself and my intention is to service Pregnant Mothers and Parents of Young Babies that would benefit from massage. I would like to have a "Home Page" and pages for "About Me", "Pregnancy Massage", "Baby Massage", a Pricing Page for Pregnancy Massage Sessions, a Pricing Page for Baby Massage Sessions, and a "Contact Me" page to allow clients to either contact me with queries or book available pregnancy massage sessions on a particular day of the week. I would also like a "News" page that would include articles I have written, news about new courses and a link to my Chatterlane page (yet to be set up). I would like to keep the colour schemes similar to my logo design colours. I need the design to be easy to follow and to appeal to a younger audience (20's to mid 30's).
The target audience is pregnant mothers-to-be wishing to receive massage treatments, and new parents and grandparents of small babies that would like to learn how to massage their babies.
The look and feel should be modern, professional, elegant and feminine.
I need the design to be in a standard format such that I can update the content by myself ( and does not need specialised software) as the company and business progresses.

Target Market(s)

Industry/Entity Type

Health And Wellness

Contact Information for Business Card

Card should have rounded edges. Design should have the same "feel" as the website. Contact Details of my business address, mobile phone, email and website should be included.

Coding

Coded - Design and coding required

Number of Pages Required

5+ page

Font styles to use
Script

Requirements
Must have
• Same colours as logo design. In cmyk system, the colours are: 20,60,0,0 which best result is tintora 681 and 40,40,0,0 which best result is tintora 2645. Card should include the logo design.

```html
<!DOCTYPE html>
<html lang="en">
<head>
<meta charset="utf-8">
<title>Gentle Willow Pregnancy and Baby Massage – Baby Massage Sessions</title>
<link rel="stylesheet" href="https://fonts.googleapis.com/css2?family=Sue+Ellen+Francisco&family=Cabin:wght@400&family=Crimson+Text&display=swap">
<style>
  :root{
    --backdrop:#0d0d0d;
    --page:#f1e4e6;
    --teal:#8fbdb9;
    --teal-soft:#a9cbc8;
    --pink:#e07ab8;
    --pink-deep:#d95aa6;
    --violet:#9287d8;
    --heading-band:#ebcdd1;
    --title-band:#eddde1;
    --label-duration:#dca7c6;
    --value-duration:#e3a8d3;
    --label-cost:#c9a5c4;
    --value-cost:#c2aedc;
    --ink:#2c2326;
    --photo-light:#f3e0e0;
    --photo-warm:#e9c9c4;
  }
  *{box-sizing:border-box;margin:0;padding:0}
  html,body{width:1200px;height:1025px;overflow:hidden;background:var(--backdrop)}
  .stage{position:absolute;left:0;top:0;width:1440px;height:1229px;transform:scale(.83333);transform-origin:0 0}
  .phone-page{position:absolute;left:527px;top:0;width:388px;height:1229px;background:var(--page);font-family:"Cabin",sans-serif;color:var(--ink);overflow:hidden}
  .abs{position:absolute;left:0;width:388px}

  .site-header{top:0;height:44px;background:var(--teal)}
  .menu-icon{position:absolute;left:13px;top:14px}
  .brand{position:absolute;left:144px;top:0;width:100px;height:44px;display:flex;align-items:center;justify-content:center;gap:4px;font-family:"Sue Ellen Francisco",cursive;color:var(--pink-deep);font-size:13px;line-height:1}
  .brand-dot{width:8px;height:8px;border-radius:50%;background:var(--pink-deep)}
  .search-icon{position:absolute;left:339px;top:11px}

  .breadcrumb{position:absolute;left:25px;top:59px;width:107px;height:16px;background:var(--teal-soft);font-size:7px;color:var(--pink);line-height:16px;text-align:center}

  .page-title{top:89px;height:32px;background:var(--title-band);font-family:"Sue Ellen Francisco",cursive;color:var(--violet);font-size:21px;line-height:32px;text-align:center;padding-right:36px}

  .section-heading{height:33px;background:var(--heading-band);font-family:"Sue Ellen Francisco",cursive;color:var(--pink);font-size:15px;line-height:33px;padding-left:21px}

  .photo-fill{position:absolute;left:0;width:388px;background:linear-gradient(100deg,var(--page) 0%,var(--photo-light) 35%,var(--photo-warm) 70%,var(--photo-light) 100%);opacity:.85}

  .section-text{position:absolute;font-size:12px;line-height:14.5px}
  .section-text ul{list-style:none}
  .section-text li::before{content:"• "}
  .section-text .sub li{padding-left:56px}
  .section-text .sub li::before{content:"o  "}

  .price-table{position:absolute;left:0;width:388px;display:grid;border-radius:0 0 4px 4px;overflow:hidden}
  .price-table .label{text-align:right;padding-right:7px;font-size:14px}
  .price-table .cell-duration-label{background:var(--label-duration);line-height:35px}
  .price-table .cell-duration-value{background:var(--value-duration);line-height:35px;padding-left:13px;font-size:14px}
  .price-table .cell-cost-label{background:var(--label-cost);padding-top:9px}
  .price-table .cell-cost-value{background:var(--value-cost);padding:12px 0 0 4px;font-family:"Crimson Text",serif;font-size:9.5px;line-height:12px;white-space:nowrap}

  .site-footer{top:1184px;height:45px;background:var(--teal);display:flex;justify-content:space-around;align-items:center;padding:0 8px;font-size:8px;color:var(--pink-deep)}
</style>
</head>
<body>
<div class="stage">
  <main class="phone-page">

    <header class="abs site-header">
      <svg class="menu-icon" width="26" height="22" viewBox="0 0 26 22" aria-label="Menu"><g fill="#d95aa6"><rect y="1" width="26" height="4" rx="2"/><rect y="9" width="26" height="4" rx="2"/><rect y="17" width="26" height="4" rx="2"/></g></svg>
      <div class="brand"><span class="brand-dot"></span>Gentle Willow</div>
      <svg class="search-icon" width="28" height="28" viewBox="0 0 28 28" aria-label="Search"><circle cx="11" cy="11" r="8.5" fill="none" stroke="#d95aa6" stroke-width="3"/><line x1="17.5" y1="17.5" x2="26" y2="26" stroke="#d95aa6" stroke-width="4" stroke-linecap="round"/></svg>
    </header>

    <nav class="breadcrumb">Home &gt; Baby massage sessions</nav>

    <h1 class="abs page-title">Baby Massage Sessions Available</h1>

    <!-- Introductory course -->
    <h2 class="abs section-heading" style="top:122px">Introductory Baby Massage Course</h2>
    <div class="photo-fill" style="top:155px;height:182px" role="img" aria-label="Soft photo of a baby lying down receiving a gentle massage"></div>
    <div class="section-text" style="left:11px;top:163px;width:370px">
      <p>This class teaches parents and carers the brief basics of Baby massage so they can get started at home.</p>
      <p>Included in this course:</p>
      <ul>
        <li>Permission sequence</li>
        <li>Which Oils to Use</li>
        <li>When is the best time to massage your baby</li>
        <li>Contraindications (when not to massage)</li>
        <li>Basic massage techniques for:</li>
      </ul>
      <ul class="sub"><li>Legs</li><li>Abdomen</li><li>Chest</li><li>Back</li></ul>
    </div>
    <div class="price-table" style="top:337px;grid-template-columns:85px 303px;grid-template-rows:36px 59px">
      <div class="label cell-duration-label">Duration:</div>
      <div class="cell-duration-value">45-60 minutes</div>
      <div class="label cell-cost-label">Cost:</div>
      <div class="cell-cost-value">Group booking – $30 per person (minimum of 3 parents and babies)<br>Private lesson – $75<br>* Bring change mat and towel.*</div>
    </div>

    <!-- Colic relief -->
    <h2 class="abs section-heading" style="top:462px;padding-left:29px">Colic relief course</h2>
    <div class="section-text" style="left:16px;top:502px;width:366px">
      <p>This session is designed to focus on relief of colic, wind, constipation and reflux. The strokes used for relief will be discussed and demonstrated, as well as general information about Baby massage and the use of appropriate oils.</p>
    </div>
    <div class="price-table" style="top:577px;grid-template-columns:93px 295px;grid-template-rows:34px 58px">
      <div class="label cell-duration-label">Duration:</div>
      <div class="cell-duration-value">45-60 minutes</div>
      <div class="label cell-cost-label">Cost:</div>
      <div class="cell-cost-value">Group booking – $30 per person (minimum of 3 parents and babies)<br>Private lesson – $75<br>* Bring change mat and towel.*</div>
    </div>

    <!-- Ante natal -->
    <h2 class="abs section-heading" style="top:698px;padding-left:30px">Ante Natal Session</h2>
    <div class="section-text" style="left:22px;top:737px;width:362px">
      <p>Basic massage techniques are demonstrated and practised on dolls provided, so that you can start to massage your baby as soon as he/she is born.</p>
    </div>
    <div class="price-table" style="top:793px;grid-template-columns:101px 287px;grid-template-rows:34px 46px">
      <div class="label cell-duration-label">Duration:</div>
      <div class="cell-duration-value">60 minutes</div>
      <div class="label cell-cost-label">Cost:</div>
      <div class="cell-cost-value" style="padding-left:9px">Group booking- $30 per person<br>&nbsp;Private lesson $75</div>
    </div>

    <!-- Advanced -->
    <h2 class="abs section-heading" style="top:905px;padding-left:19px">Advanced Baby Massage (3 one-hour sessions)</h2>
    <div class="photo-fill" style="top:938px;height:152px" role="img" aria-label="Soft photo of a baby being massaged by a parent's hands"></div>
    <div class="section-text" style="left:18px;top:943px;width:366px">
      <p>Session 1</p>
      <p>This session covers, oils, permission sequence, contraindications for massage, massage strokes for legs, feet and buttocks. When to massage and for how long</p>
      <p>Session 2</p>
      <p>This session covers baby’s daily cycle, benefits, body cues, strokes for abdominal and chest massage, and touch relaxation.</p>
      <p>Session 3</p>
      <p>Face, arms and back. Lymphatic drainage. Review of strokes</p>
    </div>
    <div class="price-table" style="top:1090px;grid-template-columns:85px 303px;grid-template-rows:35px 59px">
      <div class="label cell-duration-label">Duration:</div>
      <div class="cell-duration-value">45-60 minutes</div>
      <div class="label cell-cost-label">Cost:</div>
      <div class="cell-cost-value">Group booking – $30 per person (minimum of 3 parents and babies)<br>Private lesson – $75<br>* Bring change mat and towel.*</div>
    </div>

    <footer class="abs site-footer">
      <span>Chatterlane</span><span>Pinboardly</span><span>Chirpwave</span><span>Circlebay</span><span>Snapframe</span>
    </footer>
  </main>
</div>
</body>
</html>
```